Plakat für Feinkosthersteller
Zielgruppe
Wir sind ein Feinkosthersteller mit Fokus auf traditionelle schwäbische Produkte, die modern interpretiert und hochwertig hergestellt werden.
Unsere Produkte werden über 24/7-Verkaufsautomaten in Berlin vertrieben.
Unsere Zielgruppe sind junge Familien, zugezogene Schwaben in Berlin sowie Berlinerinnen und Berliner, die längere Zeit im Schwabenland verbracht haben und eine emotionale Verbindung zu schwäbischen Spezialitäten haben.
Die Marke verbindet Heimatgefühl, Qualität und ehrliche Küche mit einem urbanen, zeitgemäßen Auftritt.
Aufgabenstellung
Die zentrale Botschaft des Automaten ist „Heimat auf Knopfdruck“.
Der Verkaufsautomat soll Heimatgefühl, Vertrautheit und Qualität vermitteln – gleichzeitig aber modern, urban und aufmerksamkeitsstark sein.
Das Design soll so auffällig sein, dass man beim Vorbeigehen stehen bleibt und neugierig wird. Der Automat ist 24/7 zugänglich, entsprechend darf und soll er visuell präsent und markant sein.
Pflichtelemente:
– Unser Logo inklusive Korn & Kruste (wird hochgeladen)
– Der Slogan: „Heimat auf Knopfdruck“
Farbwelt:
– Orientierung an den Farben Baden-Württembergs: Gelb und Schwarz
– Gerne kräftig und kontrastreich, aber hochwertig (nicht billig oder grell)
Stil & Wirkung:
– modern, urban, selbstbewusst
– kein Kitsch, keine Trachten- oder Folkloreoptik
– eher zeitgemäß als rustikal
– emotionale Verbindung zu schwäbischer Heimat, aber klar in Berlin verortet
Format & Anwendung:
– Design für die Außenfläche eines Verkaufsautomaten (24/7 sichtbar)
– Bitte so gestalten, dass das Layout auch aus einigen Metern Entfernung gut wirkt

```html
<!DOCTYPE html>
<html lang="de">
<head>
<meta charset="utf-8">
<title>Korn &amp; Kruste – Automatenfolie</title>
<link rel="stylesheet" href="https://fonts.googleapis.com/css2?family=Oswald:wght@300;500;700&display=swap">
<style>
  :root{
    --bg:#9a9a9a;
    --yellow:#fae21c;
    --yellow-deep:#f2cf14;
    --ink:#141414;
    --window:#a9a9aa;
    --label-text:#f2d640;
  }
  *{margin:0;padding:0;box-sizing:border-box}
  html,body{width:1000px;height:1200px;overflow:hidden;background:var(--bg)}
  body{font-family:'Oswald',sans-serif;color:var(--ink);position:relative}
  .wrap{position:absolute;left:20px;top:310px;width:960px;height:581px;background:var(--yellow);overflow:hidden}
  .texture{position:absolute;inset:0;
    background:
      linear-gradient(168deg,transparent 0 6%,rgba(20,20,20,.18) 9%,transparent 16%),
      linear-gradient(12deg,transparent 0 58%,rgba(20,20,20,.16) 64%,transparent 72%),
      linear-gradient(160deg,transparent 0 80%,rgba(20,20,20,.14) 88%,transparent 96%),
      radial-gradient(ellipse at 30% 60%,var(--yellow-deep),transparent 55%);}
  .panel{position:absolute;top:0;width:306px;height:581px}
  .panel--left{left:0}
  .panel--right{left:654px}
  .brand{position:absolute;left:92px;top:62px;width:138px;height:115px;display:flex;align-items:center;justify-content:center;text-align:center;
    font-weight:700;font-size:28px;line-height:1.05;text-transform:uppercase;border:3px solid var(--ink)}
  .slogan{position:absolute;left:61px;width:200px;text-align:center;text-transform:uppercase;font-weight:700;white-space:nowrap}
  .slogan__big{top:194px;font-size:60px;line-height:1}
  .slogan__small{top:278px;font-size:18px;font-weight:500;line-height:24px}
  .slogan__small::before,.slogan__small::after{content:"";display:inline-block;width:36px;height:4px;background:var(--ink);vertical-align:middle;margin:0 12px;border-radius:2px}
  .slogan__mid{top:308px;font-size:34px;line-height:1.1;letter-spacing:-1px}
  .badge{position:absolute;left:131px;top:379px;width:60px;height:60px;border-radius:50%;background:var(--ink);color:var(--yellow);
    display:flex;align-items:center;justify-content:center;font-weight:700;font-size:21px}
  .contact{position:absolute;top:467px;text-align:right;font-weight:500;font-size:13px;line-height:25px;white-space:nowrap}
  .panel--left .contact{right:29px}
  .panel--right .contact{right:23px}
  .machine-title{position:absolute;left:346px;width:200px;top:14px;text-align:center;font-weight:500;font-size:16px;text-transform:uppercase;white-space:nowrap}
  .machine-window{position:absolute;left:343px;top:38px;width:204px;height:350px;border:7px solid var(--ink);background:var(--window)}
  .output-label{position:absolute;left:381px;top:407px;width:132px;height:54px;background:var(--ink);color:var(--label-text);
    text-align:center;text-transform:uppercase;font-size:18px;line-height:21px;padding-top:6px}
  .output-label span{display:block}
  .output-label .l1{font-weight:300}
  .output-label .l2{font-weight:500}
  .arrows{position:absolute;left:335px;top:478px;width:220px;height:80px}
  .brand-mini{position:absolute;left:599px;top:60px;width:45px;height:36px;border:1.5px solid var(--ink);
    font-weight:700;font-size:8px;line-height:1.1;text-align:center;text-transform:uppercase;display:flex;align-items:center;justify-content:center}
</style>
</head>
<body>
<main class="wrap">
  <div class="texture" role="img" aria-label="Schwarze Pinselstrich-Textur auf gelbem Grund"></div>

  <section class="panel panel--left">
    <div class="brand">Korn<br>&amp;<br>Kruste</div>
    <div class="slogan slogan__big">Heimat</div>
    <div class="slogan slogan__small">auf</div>
    <div class="slogan slogan__mid">Knopfdruck</div>
    <div class="badge">24/7</div>
    <div class="contact">brotundbelag.de<br>@brot_und_belag<br>brotundbelag@postkiste.de</div>
  </section>

  <div class="machine-title">Heimat auf Knopfdruck</div>
  <div class="machine-window"></div>
  <div class="brand-mini">Korn<br>&amp;<br>Kruste</div>
  <div class="output-label"><span class="l1">Hier kommt</span><span class="l2">Heimat raus</span></div>
  <svg class="arrows" viewBox="0 0 220 80" aria-hidden="true">
    <path d="M6 40 C20 75 75 70 92 22" fill="none" stroke="#141414" stroke-width="6" stroke-linecap="round"/>
    <path d="M78 28 L94 8 L102 34" fill="none" stroke="#141414" stroke-width="6" stroke-linejoin="round" stroke-linecap="round"/>
    <path d="M160 70 C145 60 138 40 140 12" fill="none" stroke="#141414" stroke-width="6" stroke-linecap="round"/>
    <path d="M126 26 L140 6 L152 26" fill="none" stroke="#141414" stroke-width="6" stroke-linejoin="round" stroke-linecap="round"/>
  </svg>

  <section class="panel panel--right">
    <div class="brand">Korn<br>&amp;<br>Kruste</div>
    <div class="slogan slogan__big">Heimat</div>
    <div class="slogan slogan__small">auf</div>
    <div class="slogan slogan__mid">Knopfdruck</div>
    <div class="badge">24/7</div>
    <div class="contact">brotundbelag.de<br>@brot_und_belag<br>brotundbelag@postkiste.de</div>
  </section>
</main>
</body>
</html>
```